Bright Path Flyer Design for Virtual Online Clinic. -5.5 x 8.5 inches (half sheet)

We need a clean, modern flyer design for Bright Path, a new virtual walk-in clinic based in British Columbia. The flyer will be used in libraries, pharmacies, and community centers to help residents easily access primary care through their Bright Path NFC access card.
The flyer will ask a question : NEED A DOCTOR? This should be large and attention grabbing.
The design should clearly feature a Bright Path card image (the access card) as the centerpiece and visually show how patients can use it to book appointments. The tone should feel trustworthy, healthcare-oriented, and community-friendly — clean fonts, clear spacing, and strong readability from a distance.

Side One: This card has the NFC Access Card.
NEED A DOCTOR? (Large Font, Attention Grabbing)
How to Book an Appointment using your Bright Path Card
Step 1: Tap Your Card on Your Phone
Hold your card near the back of your phone.
It will activate automatically — no app needed.
The Bright Path scheduler will open.
Step 2: Schedule Your Appointment
Select your clinical concern.
Choose your time window.
Register (only once).
Confirm your appointment.
Step 3: Relax, we’ll take care of the rest
A doctor will call during your scheduled time.
Once booked, you’ll be able to call our office.
No emails, no texts — just a real person.
It’s that simple.
Side Two:
About Bright Path
Created by Dr. Marcus Ferrigan
Bright Path was founded to make healthcare simple and convenient. Prescription renewals. Common infections. Medical notes. And so much more.
Our doctors can address 120+ health concerns virtually — providing quality care without the waiting room. No waiting rooms. Just real doctors providing real care.
Why Patients Choose Bright Path
Easy access – book and be seen from anywhere in BC.
Effortless booking – tap your Bright Path Card to begin.
Trusted physicians – every visit is with a licensed BC family doctor.
How It Works
Book your visit — choose a time window that fits your day.
Join the queue — you’ll be called when it’s your turn.
Speak directly with your doctor — simple, secure, and stress-free.
Convenient Care for Common Concerns

Additional Details.
Please find the domain to be launched soon. I've attached the NFC card file for review, it is 85.5 mm x 54 mm. The card will be glued to the flyer.
I've attached examples of flyers but they are not the look I am seeking and I am looking for creative solutions.
Thank you!
http://brightpath-example.test/

Adult Patients in British Columbia

Healthcare

• Looking for clean lines, uniform appearance, and high legibility i.e poppins

0054AA
0677BA
7BADD7
CADEEF
E8F1F8

• Need A Doctor?
• Elegant style, not too busy, clear layout.
• Clutter, look cheap - review examples.

```html
<!DOCTYPE html>
<html lang="en">
<head>
<meta charset="utf-8">
<title>Bright Path – Clinic Flyers</title>
<link href="https://fonts.googleapis.com/css2?family=Poppins:wght@400;500;600;700&family=Great+Vibes&display=swap" rel="stylesheet">
<style>
:root{
  --navy:#283b8e;
  --yellow:#f6f33c;
  --ink:#1d1d2b;
  --white:#ffffff;
  --panel:#f1f1f6;
  --rule:#d8d8e0;
  --footer:#565656;
  --stage:#a8a8a8;
  --photo-a:#8ea0c8;
  --photo-b:#c9d2e6;
  --portrait-a:#e9ecf1;
  --portrait-b:#c6ccd8;
}
*{box-sizing:border-box;margin:0;padding:0}
html,body{width:1200px;height:821px;overflow:hidden}
body{background:var(--stage);font-family:'Poppins',sans-serif;color:var(--ink);position:relative}
.flyer{position:absolute;top:57px;width:521px;height:674px;background:var(--white);overflow:hidden}
.flyer--front{left:66px}
.flyer--back{left:618px}
.abs{position:absolute}
.hero-bg{position:absolute;left:0;top:0;width:521px;height:270px}
.script{font-family:'Great Vibes',cursive;font-weight:400}

.brand{position:absolute;left:41px;font-weight:600;font-size:20px;color:var(--white);display:flex;align-items:center;gap:8px;line-height:1}
.brand-dot{width:9px;height:9px;border-radius:50%;background:var(--white)}
.flyer--front .brand{top:42px}
.flyer--back .brand{top:62px}

.welcome{left:41px;top:68px;font-size:36px;color:var(--white);line-height:1.1}
.title-yellow{left:42px;top:110px;font-size:28px;font-weight:700;color:var(--yellow);line-height:1.1;letter-spacing:.3px}
.need-doctor{left:42px;top:148px;font-size:22px;font-weight:700;color:var(--white);line-height:1.1;letter-spacing:.3px}

.card-tab{left:240px;top:0;width:260px;height:175px;background:var(--white);border-radius:0 0 40px 40px}
.access-card{left:262px;top:42px;width:216px;height:124px;background:var(--navy);border:2px solid var(--white);box-shadow:0 2px 6px rgba(0,0,0,.35);display:flex;flex-direction:column;align-items:center;justify-content:center;color:var(--white)}
.access-card .card-name{font-weight:600;font-size:17px;display:flex;align-items:center;gap:6px}
.access-card .card-name i{width:8px;height:8px;border-radius:50%;background:var(--white);display:block}
.access-card .card-url{font-size:6.5px;margin-top:4px}
.nfc-note{left:290px;top:184px;width:160px;font-size:15.5px;font-weight:600;color:var(--yellow);text-align:center;line-height:1.25}
.howto{left:53px;top:224px;font-size:21px;font-weight:500;line-height:1.2;color:var(--ink)}
.howto .accent{color:var(--navy)}

.step{position:absolute;top:332px;width:142px;height:139px;border-radius:10px 10px 0 0;background:var(--navy);color:var(--white)}
.step--yellow{background:var(--yellow);color:var(--navy)}
.step-badge{position:absolute;top:-13px;left:50%;transform:translateX(-50%);background:var(--yellow);color:var(--navy);font-weight:700;font-size:11px;padding:1px 6px;border-radius:8px;display:flex;align-items:center;gap:3px;white-space:nowrap}
.step--yellow .step-badge{background:var(--navy);color:var(--white)}
.step-badge b{width:12px;height:12px;border-radius:50%;background:var(--navy);color:var(--white);font-size:8.5px;display:flex;align-items:center;justify-content:center}
.step--yellow .step-badge b{background:var(--white);color:var(--navy)}
.step-icon{position:absolute;top:14px;left:50%;transform:translateX(-50%)}
.step-title{position:absolute;top:62px;left:0;right:0;text-align:center;font-weight:500;font-size:12px;line-height:1.2}
.step-body{position:absolute;left:10px;width:122px;top:105px;height:156px;background:var(--white);border-radius:12px 12px 10px 10px;border:2px solid var(--yellow);border-top:none;box-shadow:0 1px 3px rgba(0,0,0,.18);color:var(--ink);list-style:none}
.step--yellow .step-body{border-color:var(--navy)}
.step-body::before{content:"";position:absolute;left:17px;top:20px;bottom:22px;width:1px;background:var(--rule)}
.step-body li{position:absolute;left:12px;right:5px;font-size:10px;line-height:1.2;padding-left:12px}
.tick{display:inline-block;width:8px;height:8px;border-radius:50%;background:var(--navy);position:relative;flex:none}
.tick::after{content:"";position:absolute;left:2.5px;top:1.3px;width:2px;height:3.5px;border:solid var(--white);border-width:0 1.2px 1.2px 0;transform:rotate(45deg)}
.step-body li .tick{position:absolute;left:0;top:3px}

.help-bar{position:absolute;left:40px;top:603px;width:443px;height:24px;background:var(--yellow);border-radius:4px;font-size:10.3px;font-weight:500;white-space:nowrap;display:flex;align-items:center;justify-content:center;z-index:2;color:var(--ink)}
.footer{position:absolute;left:0;bottom:0;width:521px;height:57px;background:var(--footer);display:flex;align-items:flex-end;padding:0 0 17px 54px;gap:14px;color:var(--white);font-size:12px;font-weight:500}
.footer span{display:flex;align-items:center;gap:6px}
.footer i{width:13px;height:13px;border-radius:50%;background:var(--yellow);display:block;position:relative}
.footer i::after{content:"";position:absolute;left:3px;top:4px;width:7px;height:5px;background:var(--navy);border-radius:1px}
.footer i.web::after{left:3px;top:3px;width:7px;height:7px;border-radius:50%}

/* side two */
.portrait-frame{left:276px;top:22px;width:206px;height:216px;border:4px solid var(--white);border-radius:50% 0 50% 50%;background:var(--navy);padding:6px}
.portrait{width:100%;height:100%;border-radius:50% 0 50% 50%;background:linear-gradient(160deg,var(--portrait-a),var(--portrait-b))}
.about{left:42px;top:94px;font-size:38px;color:var(--yellow);line-height:1}
.about-title{left:42px;top:132px;font-size:28px;font-weight:700;color:var(--white);line-height:1}
.created{left:42px;top:166px;font-size:18px;font-weight:500;color:var(--white);line-height:1.2}
.name-bar{left:40px;top:193px;width:270px;height:32px;background:var(--yellow);display:flex;align-items:center;padding-left:7px;font-weight:700;font-size:21px;color:var(--ink)}
.fact-list{left:42px;top:268px;width:216px;list-style:none}
.fact-list li{display:flex;gap:5px;font-size:8.8px;font-weight:600;line-height:1.15;padding:3px 0 5px;border-bottom:1px solid var(--rule);align-items:flex-start}
.fact-list li .tick{margin-top:2px}
.photo{top:373px;width:112px;height:86px;border-radius:10px;background:linear-gradient(135deg,var(--photo-a),var(--photo-b))}
.why-title{left:40px;top:468px;font-size:13px;font-weight:600;color:var(--navy)}
.why-row{position:absolute;left:40px;width:224px;height:31px;border:1.5px solid var(--navy);border-radius:6px;display:flex;overflow:hidden;background:var(--white)}
.why-row .label{width:84px;background:var(--navy);color:var(--white);font-size:9.5px;line-height:1.1;display:flex;align-items:center;gap:6px;padding-left:6px;border-radius:0 8px 8px 0}
.why-row .label .tick{background:var(--yellow);width:10px;height:10px}
.why-row .label .tick::after{border-color:var(--navy);left:3.3px;top:1.8px}
.why-row .desc{font-size:8.5px;line-height:1.15;padding-left:10px;display:flex;align-items:center}
.side-panel{left:276px;top:240px;width:245px;height:380px;background:var(--panel)}
.address{left:311px;top:247px;font-size:11.5px;font-weight:600}
.count-box{left:308px;top:266px;width:171px;height:30px;background:var(--yellow);border-radius:4px;display:flex;align-items:center;gap:5px;padding-left:8px}
.count-box strong{font-size:26px;font-weight:700;color:var(--navy);line-height:1}
.count-box span{font-size:10.5px;font-weight:600;color:var(--navy);line-height:1.05}
.side-list{left:311px;top:305px;width:170px;list-style:none}
.side-list li{display:flex;gap:6px;font-size:8.8px;font-weight:500;line-height:1.1;margin-bottom:9px}
.side-list li .tick{margin-top:2px}
.works{left:304px;top:398px;width:168px;height:193px;border:2px solid var(--navy);border-radius:14px;background:var(--white);overflow:hidden}
.works h3{background:var(--navy);color:var(--white);font-size:14px;font-weight:600;height:32px;padding:7px 0 0 18px;border-radius:0 0 14px 14px}
.works-item{position:absolute;left:8px;display:flex;gap:8px;width:152px}
.works-item .ico{width:20px;height:20px;border-radius:50%;background:var(--yellow);border:1.5px solid var(--navy);flex:none;margin-top:2px}
.works-item p{font-size:9px;font-weight:600;line-height:1.15}
.works-item p b{color:var(--navy);font-weight:600;display:block}
</style>
</head>
<body>

<!-- Side one -->
<section class="flyer flyer--front">
  <svg class="hero-bg" viewBox="0 0 521 270" aria-hidden="true">
    <path d="M0 0H521V210C470 240 420 262 350 258C270 254 240 208 160 200C90 194 40 225 0 250Z" fill="var(--navy)"/>
    <path d="M0 250C40 225 90 194 160 200C240 208 270 254 350 258C420 262 470 240 521 210" fill="none" stroke="var(--yellow)" stroke-width="5"/>
  </svg>
  <div class="abs card-tab"></div>
  <div class="abs access-card" role="img" aria-label="Bright Path NFC access card">
    <div class="card-name"><i></i>Bright Path</div>
    <div class="card-url">www.brightpath-example.test</div>
  </div>
  <div class="brand"><span class="brand-dot"></span>Bright Path</div>
  <div class="abs script welcome">Welcome To</div>
  <div class="abs title-yellow">BRIGHT PATH</div>
  <h1 class="abs need-doctor">NEED A DOCTOR?</h1>
  <div class="abs nfc-note">This card has the<br>NFC Access Card.</div>
  <h2 class="abs howto">How to Book<br>an Appointment<br><span class="accent">using your Bright Path Card</span></h2>

  <div class="step" style="left:42px">
    <div class="step-badge">STEP <b>1</b></div>
    <svg class="step-icon" width="38" height="38" viewBox="0 0 38 38" aria-hidden="true">
      <rect x="14" y="3" width="17" height="32" rx="3" fill="none" stroke="#fff" stroke-width="2"/>
      <rect x="5" y="10" width="12" height="18" rx="2" fill="#fff"/>
      <path d="M23 12h4M23 16h4" stroke="#fff" stroke-width="1.5"/>
    </svg>
    <div class="step-title">Tap Your Card<br>on Your Phone</div>
    <ul class="step-body">
      <li style="top:15px"><span class="tick"></span>Hold your card near the back of your phone.</li>
      <li style="top:64px"><span class="tick"></span>It will activate automatically — no app needed.</li>
      <li style="top:114px"><span class="tick"></span>The Bright Path scheduler will open.</li>
    </ul>
  </div>

  <div class="step step--yellow" style="left:190px">
    <div class="step-badge">STEP <b>2</b></div>
    <svg class="step-icon" width="38" height="38" viewBox="0 0 38 38" aria-hidden="true">
      <rect x="3" y="4" width="24" height="30" rx="2" fill="none" stroke="#283b8e" stroke-width="2"/>
      <circle cx="15" cy="15" r="5" fill="none" stroke="#283b8e" stroke-width="2"/>
      <path d="M7 30c1-6 15-6 16 0" fill="none" stroke="#283b8e" stroke-width="2"/>
      <rect x="24" y="14" width="12" height="11" rx="1" fill="#fff" stroke="#283b8e" stroke-width="1.6"/>
      <path d="M24 18h12" stroke="#283b8e" stroke-width="1.4"/>
    </svg>
    <div class="step-title">Schedule Your<br>Appointment</div>
    <ul class="step-body">
      <li style="top:15px"><span class="tick"></span>Select your clinical concern.</li>
      <li style="top:52px"><span class="tick"></span>Choose your time window.</li>
      <li style="top:89px"><span class="tick"></span>Register (only once).</li>
      <li style="top:126px"><span class="tick"></span>Confirm your appointment.</li>
    </ul>
  </div>

  <div class="step" style="left:337px">
    <div class="step-badge">STEP <b>3</b></div>
    <svg class="step-icon" width="38" height="38" viewBox="0 0 38 38" aria-hidden="true">
      <rect x="3" y="6" width="24" height="18" rx="2" fill="none" stroke="#fff" stroke-width="2"/>
      <path d="M12 30h6M15 24v6" stroke="#fff" stroke-width="2"/>
      <circle cx="15" cy="13" r="3" fill="#fff"/>
      <path d="M10 22c1-4 9-4 10 0" fill="#fff"/>
      <rect x="25" y="2" width="11" height="9" rx="1" fill="#fff"/>
    </svg>
    <div class="step-title">Relax, we’ll take<br>care of the rest</div>
    <ul class="step-body">
      <li style="top:15px"><span class="tick"></span>A doctor will call during your scheduled time.</li>
      <li style="top:64px"><span class="tick"></span>Once booked, you’ll be able to call our office.</li>
      <li style="top:114px"><span class="tick"></span>No emails, no texts — just a real person.</li>
    </ul>
  </div>

  <svg class="abs" style="left:0;top:0" width="521" height="674" aria-hidden="true">
    <path d="M176 586C184 586 188 580 188 566V515H196" fill="none" stroke="var(--navy)" stroke-width="1.6"/>
    <path d="M195 511l6 4-6 4z" fill="var(--navy)"/>
    <path d="M324 586C332 586 335 580 335 566V515H343" fill="none" stroke="var(--navy)" stroke-width="1.6"/>
    <path d="M342 511l6 4-6 4z" fill="var(--navy)"/>
  </svg>

  <div class="help-bar">If you’re having trouble with your card or the access page, we’re here to help</div>
  <footer class="footer">
    <span><i></i>support@brightpath-example.test</span>
    <span><i class="web"></i>www.brightpath-example.test</span>
  </footer>
</section>

<!-- Side two -->
<section class="flyer flyer--back">
  <svg class="hero-bg" viewBox="0 0 521 270" aria-hidden="true">
    <path d="M0 0H521V185C480 200 440 222 400 238C320 262 240 258 150 240C90 228 40 212 0 205Z" fill="var(--navy)"/>
    <path d="M0 205C40 212 90 228 150 240C240 258 320 262 400 238C440 222 480 200 521 185" fill="none" stroke="var(--yellow)" stroke-width="5"/>
  </svg>
  <div class="abs side-panel"></div>
  <div class="abs portrait-frame"><div class="portrait" role="img" aria-label="Portrait of the founding doctor in a white coat"></div></div>
  <div class="brand"><span class="brand-dot"></span>Bright Path</div>
  <div class="abs script about">About</div>
  <div class="abs about-title">BRIGHT PATH</div>
  <div class="abs created">CREATED BY</div>
  <div class="abs name-bar">Dr. Marcus Ferrigan</div>

  <ul class="abs fact-list">
    <li><span class="tick"></span>Bright Path was founded to make healthcare simple and convenient.</li>
    <li><span class="tick"></span>Prescription renewals.</li>
    <li><span class="tick"></span>Common infections.</li>
    <li><span class="tick"></span>Medical notes. And so much more.</li>
  </ul>

  <div class="abs photo" style="left:40px" role="img" aria-label="Patient on a video call with a doctor on a laptop"></div>
  <div class="abs photo" style="left:159px" role="img" aria-label="Doctor taking notes during a virtual visit"></div>

  <h3 class="abs why-title">Why Patients Choose Bright Path</h3>
  <div class="why-row" style="top:493px"><div class="label"><span class="tick"></span>Easy<br>access</div><div class="desc">Book and be seen<br>from anywhere in BC.</div></div>
  <div class="why-row" style="top:527px"><div class="label"><span class="tick"></span>Effortless<br>booking</div><div class="desc">Tap your Bright Path<br>Card to begin.</div></div>
  <div class="why-row" style="top:562px"><div class="label"><span class="tick"></span>Trusted<br>physicians</div><div class="desc">Every visit is with a<br>licensed BC family doctor.</div></div>

  <div class="abs address">Our doctors can address</div>
  <div class="abs count-box"><strong>120+</strong><span>Health concerns<br>virtually</span></div>
  <ul class="abs side-list">
    <li><span class="tick"></span>Providing quality care without the waiting room.</li>
    <li><span class="tick"></span>No waiting rooms.</li>
    <li><span class="tick"></span>Just real doctors providing real care.</li>
  </ul>

  <div class="abs works">
    <h3>How It Works</h3>
    <div class="works-item" style="top:46px"><span class="ico"></span><p><b>Book your visit</b>choose a time window that fits your day.</p></div>
    <div class="works-item" style="top:88px"><span class="ico"></span><p><b>Join the queue</b>you’ll be called when it’s your turn.</p></div>
    <div class="works-item" style="top:132px"><span class="ico"></span><p><b>Speak directly with your doctor</b>simple, secure, and stress-free.</p></div>
  </div>

  <div class="help-bar">If you’re having trouble with your card or the access page, we’re here to help</div>
  <footer class="footer">
    <span><i></i>support@brightpath-example.test</span>
    <span><i class="web"></i>www.brightpath-example.test</span>
  </footer>
</section>

</body>
</html>
```